Holvern Incorporated

Holvern is a business that provides consulting, and manages and supplies trades persons in the construction and heavy industries sector. We build, do maintenance, install machinery, and can manage projects or jobs. Would like or prefer more clean, classic designs. Blacks/greys, but open to almost anything.

Target Market(s)

Industrial/Construction/Manufacturing

Industry/Entity Type

Construction Company

Contact Information for Business Card

Clean, business name on the front, possibly have the details on the back, but open to any ideas.

Logo Text

We currently do not have a slogan, open to ideas

Font styles to use
Serif
Sans Serif

Colors

Designer to choose colors to be used in the design.

Requirements
Should not have
• the oval is not my logo, was just an idea. please don't send 20 designs with the oval

```html
<!DOCTYPE html>
<html lang="en">
<head>
<meta charset="UTF-8">
<title>Holvern Incorporated – Business Card</title>
<link href="https://fonts.googleapis.com/css2?family=Open+Sans:wght@400;600;700&display=swap" rel="stylesheet">
<style>
  :root {
    --backdrop: #d6d6d6;
    --card-light: #ffffff;
    --card-dark: #2c2c2e;
    --ink: #111111;
    --ink-soft: #6a6a6a;
    --rule: #1a1a1a;
    --deboss: #1f1f21;
    --deboss-text: #3b3b3e;
  }
  * { margin: 0; padding: 0; box-sizing: border-box; }
  html, body { width: 1200px; height: 801px; overflow: hidden; }
  body {
    background: var(--backdrop);
    font-family: "Open Sans", Arial, sans-serif;
    position: relative;
  }
  .card {
    position: absolute;
    top: 252px;
    width: 520px;
    height: 297px;
    box-shadow: 0 10px 24px rgba(0,0,0,0.18);
  }
  .card--front { left: 50px; background: var(--card-light); }
  .card--back { left: 630px; background: var(--card-dark); }

  .brand {
    position: absolute;
    left: 0; top: 0;
    width: 270px; height: 297px;
    display: flex; align-items: center; justify-content: center;
    gap: 12px;
  }
  .brand__mark {
    width: 14px; height: 14px; border-radius: 50%;
    background: var(--ink);
  }
  .brand__name {
    font-weight: 700;
    font-size: 40px;
    letter-spacing: 0.5px;
    color: var(--ink);
  }

  .divider {
    position: absolute;
    left: 276px; top: 64px;
    width: 1px; height: 168px;
    background: var(--rule);
  }
  .contact {
    position: absolute;
    left: 292px; top: 62px;
    color: var(--ink-soft);
    font-size: 13.5px;
    line-height: 1.45;
  }
  .contact__name {
    font-weight: 700;
    font-size: 19px;
    color: var(--ink);
    letter-spacing: 0.2px;
    line-height: 1.2;
  }
  .contact__role { margin-bottom: 10px; }
  .contact__address { margin-bottom: 10px; }
  .contact__line { display: flex; align-items: center; gap: 6px; }
  .contact__line svg { width: 11px; height: 11px; fill: var(--ink); flex: none; }

  .deboss {
    position: absolute;
    left: 50%; top: 50%;
    transform: translate(-50%, -50%);
    display: flex; align-items: center; gap: 14px;
  }
  .deboss__mark {
    width: 16px; height: 16px; border-radius: 50%;
    background: var(--deboss);
  }
  .deboss__name {
    font-weight: 700;
    font-size: 48px;
    color: var(--deboss-text);
    letter-spacing: 0.5px;
  }
</style>
</head>
<body>
  <section class="card card--front">
    <div class="brand">
      <span class="brand__mark"></span>
      <span class="brand__name">Holvern</span>
    </div>
    <div class="divider"></div>
    <div class="contact">
      <p class="contact__name">DANIEL ASHCOMBE</p>
      <p class="contact__role">President</p>
      <p class="contact__address">18420 Ridgeview Harbor<br>Port Alden CA 90417</p>
      <p class="contact__line">
        <svg viewBox="0 0 24 24"><path d="M6.6 10.8a15.1 15.1 0 0 0 6.6 6.6l2.2-2.2a1 1 0 0 1 1-.25 11.4 11.4 0 0 0 3.6.57 1 1 0 0 1 1 1V20a1 1 0 0 1-1 1A17 17 0 0 1 3 4a1 1 0 0 1 1-1h3.5a1 1 0 0 1 1 1c0 1.25.2 2.45.57 3.57a1 1 0 0 1-.25 1z"/></svg>
        555-318-2047
      </p>
      <p class="contact__line">
        <svg viewBox="0 0 24 24"><path d="M2 5h20v14H2z M3 6l9 7 9-7" fill="none" stroke="#111" stroke-width="2.4"/></svg>
        info@holvern.com
      </p>
      <p class="contact__line">
        <svg viewBox="0 0 24 24"><circle cx="12" cy="12" r="9" fill="none" stroke="#111" stroke-width="2.4"/><path d="M3 12h18M12 3c3 3 3 15 0 18M12 3c-3 3-3 15 0 18" fill="none" stroke="#111" stroke-width="1.8"/></svg>
        www.holvern.com
      </p>
    </div>
  </section>

  <section class="card card--back">
    <div class="deboss">
      <span class="deboss__mark"></span>
      <span class="deboss__name">Holvern</span>
    </div>
  </section>
</body>
</html>
```